Higher $ Now Guaranteed! Redesign Web Page(s) Style Composition and Color (Graphics design-not code)

We need a modern look for an existing website. You can either use or change the current logo. Choice of colors, fonts, style is up to you. Sample URLs and additional details are provided in the attached document. Most of our struggle has been the appearance of the directory listings (city) page.
----------------------------------------------------------------------------------
--> Increased Project Budget and Now Funds are GUARANTEED
--> Added an additional attachment in response to questions
-->THIS PROJECT IS FOR GRAPHICS/DESIGN NOT CODE
The project is mostly a few areas of text and colored boxes or lines. Hopefully a skilled designer can place these elements in an attractive layout and choose the right colors and styles. There are no complex drawings required for this project.

*** We are involved with other projects from time to time and expect that the winning designer will be given the first opportunity at this future work. ***

*** There is no requirement to do any code but if you submit a design feel free to indicate if you wish to be considered for any future code work on this site or others ***

Font styles to use
Sans Serif

Requirements
Must have
• Rounded corners on images and buttons with nice gradients or hover effects.
Nice to have
• Attached an additional descriptions document to help with these answers.
Should not have
• Small fonts, traditional older looking rectangular buttons, dull or boring color schemes

```html
<!DOCTYPE html>
<html lang="en">
<head>
<meta charset="utf-8">
<title>LedgerScout – Bellevue Tax Preparers</title>
<link href="https://fonts.googleapis.com/css2?family=Raleway:wght@400;500;600;700&display=swap" rel="stylesheet">
<style>
:root{
  --yellow:#f2b01e;
  --yellow-dark:#c7900f;
  --navy:#1c2b35;
  --green:#7cbf3f;
  --teal:#4dc3c8;
  --teal-dark:#2f9ea3;
  --grey-head:#555759;
  --text:#444;
  --muted:#8a8a8a;
  --band:#ebebeb;
  --page:#f7f7f7;
}
*{margin:0;padding:0;box-sizing:border-box}
html,body{width:983px;height:1200px;overflow:hidden}
body{font-family:'Raleway',sans-serif;color:var(--text);background:#fff;position:relative}
.abs{position:absolute}
.top{position:absolute;left:0;top:0;width:983px;height:479px;background:var(--page)}
.brand{left:70px;top:26px;font-size:21px;font-weight:600;color:var(--navy);display:flex;align-items:center;gap:7px}
.brand-dot{width:14px;height:14px;border-radius:50%;background:var(--teal)}
.nav{left:347px;top:32px;display:flex;gap:26px;font-size:11px;font-weight:500;color:#555;letter-spacing:.2px}
.nav-search{left:704px;top:32px}
.nav-sep{left:747px;top:27px;width:1px;height:22px;background:#ddd}
.phone{left:776px;top:28px;display:flex;align-items:center;gap:8px;font-size:17px;font-weight:600;color:#3a4d5a}
.rule{left:70px;top:75px;width:843px;height:1px;background:#ddd}
.finder{left:70px;top:104px;width:430px;height:323px;background:var(--band);border-radius:4px}
.searchbox{left:83px;top:117px;width:406px;height:43px;background:#fff;border-radius:3px;display:flex;align-items:center;padding:0 14px;gap:10px;font-size:11px;font-weight:500;color:#555}
.searchbox .caret{margin-left:auto}
.card{position:absolute;width:198px;background:#fff;border-radius:4px;overflow:hidden;text-align:center}
.card h3{height:45px;display:flex;align-items:center;justify-content:center;padding:0 12px;font-size:12.5px;font-weight:700;color:#fff;line-height:1.25;text-transform:uppercase}
.card p{font-size:10.5px;line-height:13px;padding-top:10px;color:#555}
.small{height:114px}
.h-yellow{background:var(--yellow)}
.h-navy{background:var(--navy)}
.h-green{background:var(--green)}
.h-teal{background:var(--teal)}
.h-grey{background:var(--grey-head)}
.scroll{left:83px;top:420px;width:406px;height:3px;background:#d2d2d2;border-radius:2px}
.scroll i{display:block;width:42px;height:3px;background:#888;border-radius:2px}
.promo{position:absolute;border-radius:4px;overflow:hidden;color:#fff}
.promo h2{font-size:12.5px;font-weight:700;text-transform:uppercase;line-height:16px;margin-bottom:6px}
.promo p{font-size:10.5px;line-height:13px}
.btn{position:absolute;height:27px;border-radius:4px;font-size:9px;font-weight:700;color:#fff;display:flex;align-items:center;justify-content:center;letter-spacing:.3px}
.photo{position:absolute;top:0;height:153px}
.band{left:0;top:479px;width:983px;height:325px;background:var(--band)}
.reviews{left:0;top:848px;width:983px;text-align:center}
.reviews h2{font-size:21px;font-weight:600;color:var(--navy);text-transform:uppercase}
.reviews .sub{font-size:10px;color:#999;text-transform:uppercase;margin-top:2px}
.reviews hr{border:0;height:1px;background:#e3e3e3;width:652px;margin:8px auto 0}
.reviews .quote{font-size:11px;line-height:13px;color:#555;width:660px;margin:26px auto 0}
.reviews .by{font-size:11px;color:#333;margin-top:15px;font-weight:500}
.dots{display:flex;justify-content:center;gap:6px;margin-top:36px}
.dots i{width:9px;height:9px;border-radius:50%;background:#e6e6e6}
.dots i.on{background:var(--navy)}
.footer{left:0;top:1098px;width:983px;height:102px;background:var(--navy);color:#fff}
.flinks{left:70px;top:30px;display:flex;gap:17px;font-size:11px;align-items:center}
.flinks .active{color:var(--yellow);font-weight:700}
.social{display:flex;gap:16px;margin-left:4px}
.social i{width:9px;height:9px;border-radius:50%;background:#fff}
.fcopy{left:70px;top:58px;font-size:11px;word-spacing:1px}
.fcopy span{margin:0 10px}
.fbrand{left:797px;top:34px;font-size:19px;font-weight:600;display:flex;align-items:center;gap:6px}
</style>
</head>
<body>
<section class="top">
  <div class="abs brand">LedgerScout <span class="brand-dot"></span></div>
  <nav class="abs nav"><span>HOME</span><span>ABOUT US</span><span>HOW IT WORKS</span><span>CONTACT US</span></nav>
  <svg class="abs nav-search" width="13" height="13" viewBox="0 0 13 13"><circle cx="5.5" cy="5.5" r="4" fill="none" stroke="#3a4d5a" stroke-width="1.6"/><line x1="8.5" y1="8.5" x2="12" y2="12" stroke="#3a4d5a" stroke-width="1.6"/></svg>
  <div class="abs nav-sep"></div>
  <div class="abs phone">
    <svg width="18" height="18" viewBox="0 0 24 24"><path d="M6.6 10.8a15 15 0 0 0 6.6 6.6l2.2-2.2a1 1 0 0 1 1-.25 11.4 11.4 0 0 0 3.6.6 1 1 0 0 1 1 1V20a1 1 0 0 1-1 1A17 17 0 0 1 3 4a1 1 0 0 1 1-1h3.5a1 1 0 0 1 1 1c0 1.25.2 2.45.6 3.6a1 1 0 0 1-.25 1z" fill="#2a3c48"/></svg>
    860-555-0148
  </div>
  <div class="abs rule"></div>

  <div class="abs finder"></div>
  <div class="abs searchbox">
    <svg width="12" height="12" viewBox="0 0 13 13"><circle cx="5.5" cy="5.5" r="4" fill="none" stroke="#555" stroke-width="1.5"/><line x1="8.5" y1="8.5" x2="12" y2="12" stroke="#555" stroke-width="1.5"/></svg>
    BELLEVUE
    <svg class="caret" width="12" height="7" viewBox="0 0 12 7"><path d="M0 0h12L6 7z" fill="#888"/></svg>
  </div>
  <article class="card small" style="left:83px;top:171px"><h3 class="h-yellow">Harbor Line Tax Service</h3><p>214 Alder Rd,<br>WA 98004<br>Phone: (808) 555-0192</p></article>
  <article class="card small" style="left:291px;top:171px"><h3 class="h-navy">QR Tax Service</h3><p>38 Birch St,<br>WA 98004<br>Phone: (808) 555-0192</p></article>
  <article class="card small" style="left:83px;top:296px"><h3 class="h-green">Marlow Dana K CPA</h3><p>450 E Lake St Ste 208,<br>WA 98004<br>Phone: (808) 555-0192</p></article>
  <article class="card small" style="left:291px;top:296px"><h3 class="h-teal">Venner Accounting &amp; Tax Service</h3><p>712 N Cedar Ln<br>Yakima, WA 98004<br>Phone: (808) 555-0192</p></article>
  <div class="abs scroll"><i></i></div>

  <div class="promo" style="left:515px;top:104px;width:398px;height:153px;background:var(--yellow)">
    <div class="photo" role="img" aria-label="Photo of a hand signing documents at a desk" style="left:0;width:145px;background:linear-gradient(135deg,#c9733a,#e9dccb 60%,#8d6a52)"></div>
    <div class="abs" style="left:159px;top:14px;width:228px">
      <h2>Are you a tax preparer?</h2>
      <p>Our directories of tax professionals give you immediate access to new clients and prospects looking for income tax preparation and tax services in your local area.</p>
    </div>
    <div class="btn" style="left:159px;top:104px;width:149px;background:var(--yellow-dark)">SUBMIT LISTING</div>
  </div>

  <div class="promo" style="left:516px;top:275px;width:397px;height:153px;background:var(--teal)">
    <div class="abs" style="left:15px;top:12px;width:230px">
      <h2>Have a local tax firm<br>contact me</h2>
      <p>Our directories of tax professionals give you immediate access to the very best tax preparers and income tax advisors in your area.</p>
    </div>
    <div class="btn" style="left:15px;top:112px;width:148px;background:var(--teal-dark)">GET STARTED</div>
    <div class="photo" role="img" aria-label="Photo of hands reviewing tax forms beside a calculator" style="left:253px;width:144px;background:linear-gradient(135deg,#b0562a,#f1ede6 45%,#7b4a30)"></div>
  </div>
</section>

<section class="abs band">
  <article class="card" style="left:79px;top:38px;height:115px"><h3 class="h-grey">Orlan, Peter,<br>CPA</h3><p>320 W Maple St<br>Bellevue, WA 98004<br>Phone: (623) 555-0130</p></article>
  <article class="card" style="left:288px;top:38px;height:115px"><h3 class="h-grey">Tessman Rowe of Bellevue</h3><p>145 E Harbor Ave<br>Bellevue, WA 98004<br>Phone: (623) 555-0137</p></article>
  <article class="card" style="left:497px;top:38px;height:115px"><h3 class="h-grey">Bookkeeping<br>Service</h3><p>2210 N Ridge Rd<br>Ste A3<br>Bellevue, WA 98004<br>Phone: (623) 555-0157</p></article>
  <article class="card" style="left:706px;top:38px;height:115px"><h3 class="h-grey">Hale-Winters Accounting</h3><p>2210 N Central Ave<br>Bellevue, WA 98004<br>Phone: (623) 555-0110</p></article>
  <article class="card" style="left:79px;top:165px;height:115px"><h3 class="h-grey">Nora Quill and<br>Company</h3><p>2210 N Ridge Rd<br>Ste A3<br>Bellevue, WA 98004<br>Phone: (623) 555-0157</p></article>
  <article class="card" style="left:288px;top:165px;height:115px"><h3 class="h-grey">Lindqvist Mara CPA PC</h3><p>145 E Harbor Ave<br>Bellevue, WA 98004<br>Phone: (623) 555-0137</p></article>
</section>

<section class="abs reviews">
  <h2>See what our tax preparers says</h2>
  <div class="sub">Taxpayers estimonials</div>
  <hr>
  <p class="quote">Lorem Ipsum is simply dummy text of the printing and typesetting industry. Lorem Ipsum has been the industry's standard dummy text ever since the 1500s, when an unknown printer took a galley of type and scrambled it to make a type specimen book.</p>
  <p class="by">by - Lorem Ipsum</p>
  <div class="dots"><i></i><i class="on"></i><i></i></div>
</section>

<footer class="abs footer">
  <div class="abs flinks">
    <span>Home</span><span>Navigation</span><span class="active">Directory</span><span>Special Offers</span><span>Contact Us</span>
    <span class="social"><i></i><i></i><i></i></span>
  </div>
  <div class="abs fcopy">© All Rights Reserved. Design by www.ledgerscout.com <span>|</span> PO Box 4417 <span>|</span> Milford, CT <span>|</span> 06460</div>
  <div class="abs fbrand">LedgerScout <span class="brand-dot"></span></div>
</footer>
</body>
</html>
```